Thank You Card

Catering company customer Thank You cards

Thank you card to past clients after event completion

Should be on recycled or green paper.

Room to write personal message. No long prewritten messages of thanks and gratitude.

Should have Red and Zapfino fonts to match logo

Simple bold design thanking international clientele

Design could incorporate fish, knives, fire, wine, wood

No palm trees, coconuts, surfboards,beachballs or tikis

1. Please show envelope designs that match the card. 

2. Thank you going down the left side of the card cover in a column in at least 5 languages: Mahalo, Japanese, Chinese, French, Spanish, German, Italian

Company based on Oahu servicing locals and visitors

Catering

```html
<!DOCTYPE html>
<html lang="en">
<head>
<meta charset="utf-8">
<title>Thank You Card</title>
<link rel="stylesheet" href="https://fonts.googleapis.com/css2?family=Cormorant+Garamond:ital,wght@1,600&family=Noto+Serif:wght@400&family=Noto+Sans+JP:wght@500&display=swap">
<style>
  :root {
    --field-light: #f6fff2;
    --field-green: #c8fdc2;
    --stripe-red: #e9545a;
    --stripe-red-deep: #c84548;
    --stripe-brown: #7b2d0b;
    --stripe-sage: #b8e28c;
    --stripe-silver-top: #ffffff;
    --stripe-silver-bottom: #a9a9a9;
    --stripe-white: #ffffff;
    --ink-white: #ffffff;
    --ink-orange: #e8620e;
    --ink-vermilion: #d9480f;
    --ink-leaf: #3b7a17;
  }
  html, body {
    margin: 0;
    padding: 0;
    overflow: hidden;
    background: #ffffff;
  }
  .card {
    position: relative;
    width: 1200px;
    height: 716px;
    overflow: hidden;
    background: linear-gradient(100deg, var(--field-light) 35%, var(--field-green) 100%);
  }
  .stripe {
    position: absolute;
    top: 0;
    bottom: 0;
    display: flex;
    justify-content: center;
  }
  .stripe--merci   { left: 0;     width: 114px; background: linear-gradient(180deg, var(--stripe-red), var(--stripe-red-deep)); }
  .stripe--gracias { left: 114px; width: 112px; background: var(--stripe-brown); }
  .stripe--arigato { left: 226px; width: 114px; background: var(--stripe-sage); }
  .stripe--danke   { left: 340px; width: 115px; background: linear-gradient(180deg, var(--stripe-silver-top) 30%, var(--stripe-silver-bottom)); }
  .stripe--grazie  { left: 455px; width: 115px; background: var(--stripe-white); }

  .word {
    margin: 0;
    writing-mode: vertical-rl;
    text-orientation: upright;
    white-space: nowrap;
    line-height: 1;
    position: absolute;
    top: 224px;
  }
  .word--merci {
    font-family: "Cormorant Garamond", serif;
    font-style: italic;
    font-weight: 600;
    font-size: 54px;
    letter-spacing: -8px;
    color: var(--ink-white);
  }
  .word--gracias {
    font-family: "Noto Serif", serif;
    font-size: 58px;
    letter-spacing: -32px;
    color: var(--ink-white);
  }
  .word--arigato {
    top: 226px;
    font-family: "Noto Sans JP", sans-serif;
    font-weight: 500;
    font-size: 38px;
    letter-spacing: 5px;
    color: var(--ink-vermilion);
  }
  .word--danke {
    font-family: "Noto Serif", serif;
    font-size: 62px;
    letter-spacing: -30px;
    color: var(--ink-orange);
  }
  .word--grazie {
    font-family: "Cormorant Garamond", serif;
    font-style: italic;
    font-weight: 600;
    font-size: 48px;
    letter-spacing: -7px;
    color: var(--ink-leaf);
  }
  .rings {
    position: absolute;
    left: 0;
    top: 0;
    width: 1200px;
    height: 240px;
  }
</style>
</head>
<body>
  <main class="card">
    <div class="stripe stripe--merci"><p class="word word--merci" lang="fr">Merci</p></div>
    <div class="stripe stripe--gracias"><p class="word word--gracias" lang="es">Gracias</p></div>
    <div class="stripe stripe--arigato"><p class="word word--arigato" lang="ja">ありがとうございます。</p></div>
    <div class="stripe stripe--danke"><p class="word word--danke" lang="de">Danke</p></div>
    <div class="stripe stripe--grazie"><p class="word word--grazie" lang="it">Gracie</p></div>

    <svg class="rings" viewBox="0 0 1200 240" role="img" aria-label="Cluster of colourful overlapping concentric rings in red, orange, yellow, green and black across the top edge">
      <defs>
        <linearGradient id="ringsTone" x1="0" y1="0" x2="1" y2="0">
          <stop offset="0" stop-color="#c9352a"/>
          <stop offset="0.3" stop-color="#e0872e"/>
          <stop offset="0.5" stop-color="#f2e39a"/>
          <stop offset="0.7" stop-color="#d8462a"/>
          <stop offset="1" stop-color="#9b3a18"/>
        </linearGradient>
      </defs>
      <path fill="url(#ringsTone)" d="M0 0 H1040 C1050 60 1010 130 930 140 C880 150 840 150 800 205 C740 225 640 220 560 205 C520 225 470 225 440 210 C400 225 350 230 300 215 C260 225 220 222 190 205 C140 225 90 215 60 190 C30 210 10 200 0 185 Z"/>
    </svg>
  </main>
</body>
</html>
```